Building company requiring web site design

We need a web design for a new company based in Sydney called Marlow Building Co. We build and renovate new and existing homes for consumers. We would like to see design that use the colours red and grey. The final design should communicate innovative building but with old fashion quality, great customer service and attention to detail. I have already had a logo and stationary design completed and would like to use the these colour schemes
Updates

Target Market(s)

Home owners, investors

Industry/Entity Type

Building

Coding

Coded - Design and coding required

Number of Pages Required

5+ page

Requirements
Must have
• Home page, contact page, about us page, gallery page and testimonial page
Nice to have
• Contact form

```html
<!DOCTYPE html>
<html lang="en">
<head>
<meta charset="utf-8">
<title>Marlow Building Co. — Home Renovation &amp; Build</title>
<link rel="stylesheet" href="https://fonts.googleapis.com/css2?family=Raleway:wght@400;500;600&family=Roboto+Slab:wght@700&family=Open+Sans:wght@400;600&display=swap">
<style>
  :root {
    --red: #b9393d;
    --red-deep: #a82f33;
    --ink: #2b2b2b;
    --muted: #6b6b6b;
    --line: #e2e2e2;
    --paper: #ffffff;
    --grey-shape: #d9d9d9;
    --footer: #232323;
  }
  * { box-sizing: border-box; margin: 0; padding: 0; }
  html, body { width: 1200px; height: 2416px; overflow: hidden; background: var(--paper); }
  body { position: relative; font-family: "Raleway", sans-serif; color: var(--ink); }

  /* Header */
  .site-header { position: absolute; left: 0; top: 0; width: 1200px; height: 106px; background: var(--paper); }
  .brand { position: absolute; left: 186px; top: 32px; display: flex; align-items: center; gap: 10px; }
  .brand-mark { width: 14px; height: 14px; background: var(--red); flex: none; }
  .brand-name { font-family: "Raleway", sans-serif; font-weight: 600; font-size: 17px; line-height: 20px; color: var(--ink); }
  .main-nav a { position: absolute; top: 50px; color: var(--ink); text-decoration: none; font-size: 13px; font-weight: 500; letter-spacing: .3px; white-space: nowrap; }
  .main-nav a.is-active { color: var(--red); }
  .main-nav a.is-active::after { content: ""; position: absolute; left: -4px; right: -4px; top: 28px; height: 2px; background: var(--red); }
  .header-phone { position: absolute; left: 900px; top: 46px; display: flex; align-items: center; gap: 5px; color: var(--red); font-size: 18px; font-weight: 500; white-space: nowrap; }

  /* Hero */
  .hero { position: absolute; left: 0; top: 106px; width: 1200px; height: 479px;
    background: linear-gradient(180deg, #5f9bd8 0%, #8dbbe4 45%, #b57a4f 75%, #9a5f3a 100%); }
  .hero-title { position: absolute; left: 0; width: 1200px; top: 168px; text-align: center; color: #fff;
    font-family: "Roboto Slab", serif; font-weight: 700; font-size: 43px; letter-spacing: .5px; }
  .hero-sub { position: absolute; left: 0; width: 1200px; top: 225px; text-align: center; color: #fff;
    font-family: "Roboto Slab", serif; font-weight: 700; font-size: 26px; }
  .hero-dots { position: absolute; top: 448px; left: 566px; display: flex; gap: 4px; }
  .hero-dots span { width: 14px; height: 14px; border-radius: 50%; background: #fff; }
  .hero-dots span.is-off { background: transparent; border: 2px solid #fff; }

  /* Welcome */
  .welcome { position: absolute; left: 0; top: 585px; width: 1200px; height: 480px; background: #fafafa; }
  .section-title { position: absolute; left: 0; width: 1200px; text-align: center; font-size: 26px; font-weight: 400; color: var(--ink); letter-spacing: .5px; }
  .section-lead { position: absolute; left: 0; width: 1200px; text-align: center; font-family: "Open Sans", sans-serif; font-size: 13.5px; line-height: 24px; color: var(--muted); }
  .service-card { position: absolute; top: 174px; width: 252px; height: 268px; background: var(--paper);
    border: 1px solid var(--line); box-shadow: 0 2px 6px rgba(0,0,0,.08); text-align: center; }
  .service-photo { height: 167px; }
  .service-name { margin-top: 12px; font-size: 17px; font-weight: 500; }
  .service-text { margin-top: 3px; font-family: "Open Sans", sans-serif; font-size: 12px; color: var(--muted); }
  .btn-small { display: inline-block; margin-top: 10px; width: 89px; height: 25px; line-height: 25px; background: var(--red);
    color: #fff; font-family: "Open Sans", sans-serif; font-size: 10px; text-decoration: none; }

  /* Process band */
  .process { position: absolute; left: 0; top: 1066px; width: 1200px; height: 410px;
    background: linear-gradient(90deg, var(--red) 0%, var(--red) 30%, #c98063 50%, #d1a06b 62%, #6fa3d6 80%, #5b90cc 100%); }
  .process-title { position: absolute; left: 194px; top: 88px; color: #fff; font-size: 31px; font-weight: 400; }
  .process-text { position: absolute; left: 194px; top: 140px; width: 360px; color: #fff; font-family: "Open Sans", sans-serif; font-size: 13px; line-height: 24px; }
  .btn-outline { position: absolute; left: 197px; top: 262px; width: 117px; height: 34px; line-height: 32px; border: 1.5px solid #fff;
    color: #fff; text-align: center; font-family: "Open Sans", sans-serif; font-size: 14px; text-decoration: none; }

  /* Projects */
  .projects { position: absolute; left: 0; top: 1476px; width: 1200px; height: 454px; background: var(--paper); }
  .projects-ground { position: absolute; left: 30px; top: 400px; width: 1140px; height: 54px; background: linear-gradient(180deg, #e4e4e4, var(--grey-shape)); }
  .project-card { position: absolute; top: 167px; width: 226px; height: 218px;
    clip-path: polygon(11% 0, 100% 0, 95% 100%, 0 100%); background: var(--red); }
  .project-card::before { content: ""; position: absolute; left: 0; right: 0; top: 0; height: 3px; background: var(--red-deep); }
  .project-photo { position: absolute; left: 0; top: 3px; width: 100%; height: 129px; }
  .project-name { position: absolute; left: 30px; top: 144px; color: #fff; font-family: "Open Sans", sans-serif; font-size: 13px; font-weight: 600; }
  .project-text { position: absolute; left: 30px; top: 166px; width: 180px; color: #fff; font-family: "Open Sans", sans-serif; font-size: 10px; line-height: 14px; }

  /* Testimonial */
  .testimonial { position: absolute; left: 0; top: 1930px; width: 1200px; height: 354px; background: var(--paper); }
  .testimonial-photo { position: absolute; left: 0; top: 0; width: 680px; height: 354px;
    background: linear-gradient(90deg, #d8d4d0 0%, #ebe8e5 60%, rgba(255,255,255,0) 100%); }
  .testimonial-title { position: absolute; left: 568px; top: 80px; color: var(--red); font-size: 30px; font-weight: 400; }
  .testimonial-text { position: absolute; left: 572px; top: 128px; width: 430px; font-family: "Open Sans", sans-serif; font-size: 12px; line-height: 24.5px; color: var(--ink); }
  .testimonial-author { position: absolute; left: 577px; top: 240px; font-family: "Open Sans", sans-serif; font-size: 14px; color: var(--ink); }

  /* Footer */
  .site-footer { position: absolute; left: 0; top: 2284px; width: 1200px; height: 132px; background: var(--footer); }
  .footer-nav a { position: absolute; top: 40px; color: #fff; text-decoration: none; font-size: 13px; font-weight: 500; white-space: nowrap; }
  .footer-copy { position: absolute; left: 185px; top: 65px; color: #cfcfcf; font-family: "Open Sans", sans-serif; font-size: 11.5px; }
  .social { position: absolute; left: 888px; top: 38px; display: flex; gap: 5px; }
  .social span { width: 32px; height: 32px; border-radius: 50%; background: #fff; }
</style>
</head>
<body>

<header class="site-header">
  <div class="brand"><span class="brand-mark"></span><span class="brand-name">Marlow<br>Building Co.</span></div>
  <nav class="main-nav">
    <a class="is-active" href="#" style="left:385px">HOME</a>
    <a href="#" style="left:452px">ABOUT</a>
    <a href="#" style="left:525px">SERVICES</a>
    <a href="#" style="left:615px">PROJECT</a>
    <a href="#" style="left:701px">TESTIMONIAL</a>
    <a href="#" style="left:818px">CONTACT</a>
  </nav>
  <div class="header-phone">
    <svg width="16" height="16" viewBox="0 0 24 24" fill="none" stroke="currentColor" stroke-width="2" aria-hidden="true"><path d="M22 16.9v3a2 2 0 0 1-2.2 2 19.8 19.8 0 0 1-8.6-3.1 19.5 19.5 0 0 1-6-6A19.8 19.8 0 0 1 2.1 4.2 2 2 0 0 1 4.1 2h3a2 2 0 0 1 2 1.7c.1.9.4 1.8.7 2.7a2 2 0 0 1-.5 2.1L8 9.8a16 16 0 0 0 6 6l1.3-1.3a2 2 0 0 1 2.1-.4c.9.3 1.8.6 2.7.7a2 2 0 0 1 1.7 2z"/></svg>
    0400 555 018
  </div>
</header>

<section class="hero" role="img" aria-label="Photo of two builders in hard hats laying bricks on a building site under a blue sky">
  <h1 class="hero-title">HOME RENNOVATION &amp; BUILD</h1>
  <p class="hero-sub">LET PEOPLE&nbsp; CREATE &amp; SHARE CONTENT</p>
  <div class="hero-dots"><span class="is-off"></span><span></span><span></span><span></span></div>
</section>

<section class="welcome">
  <h2 class="section-title" style="top:52px">WELCOME TO MARLOW BUILDING CO.</h2>
  <p class="section-lead" style="top:88px">Cum sociis natoque penatibus et magnis dis parturient montes nascetur ridiculus mus In iaculis facilisis<br>massa Etiam eu urna Sed porta Suspendisse quam leo molestie</p>

  <article class="service-card" style="left:195px">
    <div class="service-photo" role="img" aria-label="Photo of a timber-framed house under construction" style="background:linear-gradient(180deg,#6ea6dc,#d3a86a)"></div>
    <h3 class="service-name">CONSTRUCTION</h3>
    <p class="service-text">Duis quam Nam eget lacus Aliquam</p>
    <a class="btn-small" href="#">READ MORE</a>
  </article>
  <article class="service-card" style="left:471px">
    <div class="service-photo" role="img" aria-label="Photo of exposed roof rafters in a home renovation" style="background:linear-gradient(135deg,#b86a3e,#e6c7a4)"></div>
    <h3 class="service-name">HOME RENNOVATION</h3>
    <p class="service-text">Duis quam Nam eget lacus Aliquam</p>
    <a class="btn-small" href="#">READ MORE</a>
  </article>
  <article class="service-card" style="left:746px">
    <div class="service-photo" role="img" aria-label="Photo of a builder shaking hands with a client" style="background:linear-gradient(135deg,#c9c9c9,#8e8e8e)"></div>
    <h3 class="service-name">DESIGN &amp; IDEA</h3>
    <p class="service-text">Duis quam Nam eget lacus Aliquam</p>
    <a class="btn-small" href="#">READ MORE</a>
  </article>
</section>

<section class="process" role="img" aria-label="Photo of a carpenter hammering roof trusses, tinted red on the left">
  <h2 class="process-title">How we working</h2>
  <p class="process-text">Cras a ante vitae enim iaculis aliquam Mauris nunc quam venenatis nec euismod sit amet egestas placerat est Pellentesque habitant morbi tristique senectus et netus et malesuada fames ac turpis egestas Cras</p>
  <a class="btn-outline" href="#">View More</a>
</section>

<section class="projects">
  <div class="projects-ground" role="img" aria-label="Faint grey illustration of house outlines"></div>
  <h2 class="section-title" style="top:64px">RECENT PROJECTS</h2>
  <p class="section-lead" style="top:98px;font-size:14.5px">Cum sociis natoque penatibus et magnis dis parturient montes nascetur</p>

  <article class="project-card" style="left:167px">
    <div class="project-photo" role="img" aria-label="Photo of a finished two-storey home" style="background:linear-gradient(180deg,#6fa5dc,#a79a82)"></div>
    <h3 class="project-name">Project Name</h3>
    <p class="project-text">penatibus et magnis dis parturient montes nascetur ridiculus</p>
  </article>
  <article class="project-card" style="left:380px">
    <div class="project-photo" role="img" aria-label="Photo of a home with scaffolding during renovation" style="background:linear-gradient(180deg,#7eb0e0,#b79c7e)"></div>
    <h3 class="project-name">Project Name</h3>
    <p class="project-text">penatibus et magnis dis parturient montes nascetur ridiculus</p>
  </article>
  <article class="project-card" style="left:592px">
    <div class="project-photo" role="img" aria-label="Photo of a modern home at dusk" style="background:linear-gradient(180deg,#5b6f8e,#8b8478)"></div>
    <h3 class="project-name">Project Name</h3>
    <p class="project-text">penatibus et magnis dis parturient montes nascetur ridiculus</p>
  </article>
  <article class="project-card" style="left:805px">
    <div class="project-photo" role="img" aria-label="Photo of a timber house frame" style="background:linear-gradient(180deg,#9cc0e2,#c7a57c)"></div>
    <h3 class="project-name">Project Name</h3>
    <p class="project-text">penatibus et magnis dis parturient montes nascetur ridiculus</p>
  </article>
</section>

<section class="testimonial">
  <div class="testimonial-photo" role="img" aria-label="Photo of a smiling family sitting together on a sofa at home"></div>
  <h2 class="testimonial-title">What Our Client Says</h2>
  <p class="testimonial-text">Cras a ante vitae enim iaculis aliquam Mauris nunc quam venenatis nec euismod sit amet egestas placerat est Pellentesque habitant morbi tristique senectus et netus et malesuada fames ac turpis egestas Cras id elit Integer quis urna Ut ante enim nec convallis pede venenati</p>
  <p class="testimonial-author">By Author Name</p>
</section>

<footer class="site-footer">
  <nav class="footer-nav">
    <a href="#" style="left:185px">HOME</a>
    <a href="#" style="left:252px">ABOUT</a>
    <a href="#" style="left:325px">SERVICES</a>
    <a href="#" style="left:415px">PROJECT</a>
    <a href="#" style="left:501px">TESTIMONIAL</a>
    <a href="#" style="left:617px">CONTACT</a>
  </nav>
  <p class="footer-copy">© 2016 Company Name&nbsp; All right reserved&nbsp; Term of Use</p>
  <div class="social" aria-label="Social links">
    <span></span><span></span><span></span><span></span>
  </div>
</footer>

</body>
</html>
```